Business card revamp

we are refrigeration mechanic i need a modern professional double side business card using my current branding
The card information must have site address~ 17 Pellham st cobram, Vic 3644 postal address~ P.o. Box 862 cobram,Vic 3643 Phone Number~0358941637 Fax Nunber~0358936205 Email address~ brettk@vorlatek.com.au Title~ Manager Licence numbers~ AU47319, NSW 481927D Web site~ www.frostwaylane.com.au

```html
<!DOCTYPE html>
<html lang="en">
<head>
<meta charset="utf-8">
<title>Frostwaylane – Business Card</title>
<link rel="stylesheet" href="https://fonts.googleapis.com/css2?family=Roboto:wght@300;400;500;700&display=swap">
<style>
  :root {
    --brand-blue: #0573bf;
    --brand-blue-dark: #1f5fa8;
    --brand-red: #c1272d;
    --card-white: #efefef;
    --ink: #333333;
    --logo-grey: #5a5a5a;
    --page: #e4e5e7;
    --on-blue: #ffffff;
  }
  * { box-sizing: border-box; margin: 0; padding: 0; }
  html, body {
    width: 1200px; height: 1000px; overflow: hidden;
    background: var(--page);
    font-family: "Roboto", Arial, sans-serif;
  }
  .sheet {
    position: relative; width: 1200px; height: 1000px;
  }
  .card {
    position: absolute; left: 250px; width: 700px; height: 400px;
    box-shadow: 0 6px 18px rgba(0,0,0,.18);
    overflow: hidden;
  }

  /* Front */
  .card--front { top: 60px; background: var(--brand-blue); color: var(--on-blue); }
  .front__brand {
    position: absolute; top: 110px; left: 0; right: 0; text-align: center;
  }
  .front__name {
    font-size: 66px; font-weight: 700; letter-spacing: 4px; line-height: 1;
  }
  .front__tagline {
    margin-top: 10px; font-size: 15px; font-weight: 300;
    letter-spacing: 3.2px; text-transform: uppercase;
  }
  .front__details {
    position: absolute; top: 262px; left: 0; right: 0; text-align: center;
    font-size: 19px; letter-spacing: 4px; line-height: 1.6; font-weight: 400;
  }

  /* Back */
  .card--back { top: 530px; background: var(--card-white); color: var(--ink); }
  .back__brand { position: absolute; top: 34px; left: 44px; }
  .back__name {
    font-size: 34px; font-weight: 700; letter-spacing: 2px; color: var(--logo-grey); line-height: 1;
  }
  .back__tagline {
    margin-top: 6px; font-size: 9px; letter-spacing: 1.6px; text-transform: uppercase; color: var(--logo-grey);
  }
  .person { position: absolute; top: 118px; left: 44px; }
  .person__name { font-size: 24px; font-weight: 500; }
  .person__first { color: var(--brand-red); }
  .person__last { color: var(--brand-blue-dark); }
  .person__title { margin-top: 4px; font-size: 19px; letter-spacing: 1px; }
  .postal { position: absolute; top: 204px; left: 44px; font-size: 19px; line-height: 1.35; letter-spacing: .5px; }
  .postal__label { color: var(--brand-red); }

  .contact {
    position: absolute; top: 150px; right: 40px; list-style: none;
    font-size: 19px; letter-spacing: .8px; line-height: 1.3; text-align: right;
  }
  .contact__item { display: flex; justify-content: flex-end; align-items: flex-start; gap: 12px; margin-bottom: 8px; }
  .contact__icon { width: 16px; height: 16px; flex: none; margin-top: 4px; fill: var(--brand-red); }

  .edge { position: absolute; left: 0; bottom: 0; width: 700px; height: 40px; }
</style>
</head>
<body>
<main class="sheet">

  <section class="card card--front" aria-label="Card front">
    <div class="front__brand">
      <div class="front__name">FROSTWAYLANE</div>
      <div class="front__tagline">Heating and Cooling Specialists</div>
    </div>
    <div class="front__details">
      <div>www.frostwaylane.com.au</div>
      <div>AU47319, NSW 481927D</div>
    </div>
  </section>

  <section class="card card--back" aria-label="Card back">
    <div class="back__brand">
      <div class="back__name">FROSTWAYLANE</div>
      <div class="back__tagline">Heating and Cooling Specialists</div>
    </div>

    <div class="person">
      <div class="person__name"><span class="person__first">Brett</span><span class="person__last">Kalinowski</span></div>
      <div class="person__title">Manager</div>
    </div>

    <div class="postal">
      <div class="postal__label">P.o. Box</div>
      <div>862 cobram,Vic 3643</div>
    </div>

    <ul class="contact">
      <li class="contact__item">
        <span>17 Pellham st cobram<br>Vic 3644</span>
        <svg class="contact__icon" viewBox="0 0 16 16" aria-hidden="true"><path d="M8 0a5.5 5.5 0 0 0-5.5 5.5C2.5 10 8 16 8 16s5.5-6 5.5-10.5A5.5 5.5 0 0 0 8 0zm0 7.6a2.1 2.1 0 1 1 0-4.2 2.1 2.1 0 0 1 0 4.2z"/></svg>
      </li>
      <li class="contact__item">
        <span>0358941637</span>
        <svg class="contact__icon" viewBox="0 0 16 16" aria-hidden="true"><path d="M4 0h8a1.5 1.5 0 0 1 1.5 1.5v13A1.5 1.5 0 0 1 12 16H4a1.5 1.5 0 0 1-1.5-1.5v-13A1.5 1.5 0 0 1 4 0zm.5 2v10h7V2zm3.5 11a1 1 0 1 0 0 2 1 1 0 0 0 0-2z"/></svg>
      </li>
      <li class="contact__item">
        <span>0358936205</span>
        <svg class="contact__icon" viewBox="0 0 16 16" aria-hidden="true"><path d="M4 0h8v5H4zM1.5 6h13A1.5 1.5 0 0 1 16 7.5V13h-3v3H3v-3H0V7.5A1.5 1.5 0 0 1 1.5 6zM4.5 11v3.5h7V11z"/></svg>
      </li>
      <li class="contact__item">
        <span>brettk@vorlatek.com.au</span>
        <svg class="contact__icon" viewBox="0 0 16 16" aria-hidden="true"><path d="M0 3h16v10H0zm1.6 1.4L8 9l6.4-4.6z" fill-rule="evenodd"/></svg>
      </li>
    </ul>

    <svg class="edge" viewBox="0 0 700 40" preserveAspectRatio="none" aria-hidden="true">
      <polygon points="0,4 118,4 100,40 0,40" fill="var(--brand-red)"/>
      <polygon points="124,18 700,18 700,40 112,40" fill="var(--brand-blue)"/>
    </svg>
  </section>

</main>
</body>
</html>
```